Movie Poster for Short Film Sci-Fi Drama

BrightHollow Pictures of North Carolina is making a new short film called "A Letter Under Paint".

This is short film about a lonely boy who falls in love with a girl from the past through poetry on a closet wall.

I want the poster to invoke longing and love. I want the focus of the poster to be poetry on a closet wall and I want the words from title of the movie to be part of the poetry written on the walls, but to stand out as the title somehow.

This is not a happy-go-lucky romantic comedy. The girl is from 1981 and boy is from the present era.

Because this is a promotional movie poster for a film that has not yet been shot, I do not want any humans featured in the poster. I would like to keep the focus on the handwritten poetry that sparked a romance between two teenagers decades apart in time.

I would like to have "A BrightHollow Production" at the top of the poster, please.

Target Market(s)

Teenagers upward to adults.

Industry/Entity Type

Movie Production

Requirements
Must have
• Handwriting font.
Should not have
• Humans or faces; exterior walls

```html
<!DOCTYPE html>
<html lang="en">
<head>
<meta charset="utf-8">
<title>A Letter Under Paint — Poster</title>
<link rel="stylesheet" href="https://fonts.googleapis.com/css2?family=Caveat+Brush&family=Reenie+Beanie&family=Oswald:wght@300&display=swap">
<style>
  :root {
    --wall-light: #d4d4d1;
    --wall-mid: #c2c2bf;
    --wall-dark: #a9a9a6;
    --floor: #8f8f8c;
    --ink: #1c1c1c;
    --ink-soft: #2e2e2e;
    --credit: #f2f2f0;
  }
  * { margin: 0; padding: 0; box-sizing: border-box; }
  html, body { width: 804px; height: 1200px; overflow: hidden; background: var(--wall-mid); }
  .poster {
    position: relative;
    width: 804px;
    height: 1200px;
    overflow: hidden;
  }
  .scene-photo {
    position: absolute;
    inset: 0;
    background:
      linear-gradient(180deg, transparent 0%, transparent 88%, var(--floor) 100%),
      radial-gradient(ellipse at 55% 35%, var(--wall-light) 0%, var(--wall-mid) 55%, var(--wall-dark) 100%);
  }
  .production-credit {
    position: absolute;
    top: 38px;
    left: 0;
    width: 100%;
    text-align: center;
    font-family: "Oswald", sans-serif;
    font-weight: 300;
    font-size: 18px;
    letter-spacing: 0.5px;
    color: var(--credit);
  }
  .wall-verse {
    position: absolute;
    top: 162px;
    left: 0;
    width: 100%;
    text-align: center;
    font-family: "Reenie Beanie", cursive;
    font-size: 34px;
    line-height: 40px;
    color: var(--ink-soft);
  }
  .title {
    position: absolute;
    top: 370px;
    left: 222px;
    font-family: "Caveat Brush", cursive;
    color: var(--ink);
    line-height: 1;
  }
  .title span { display: block; }
  .title-small { font-size: 78px; }
  .title-large { font-size: 150px; margin-top: -14px; }
  .title-link { font-size: 50px; margin: -18px 0 -22px 14px; }
  .title-last { margin-left: 70px; }
</style>
</head>
<body>
  <main class="poster">
    <div class="scene-photo" role="img" aria-label="Photograph of a bare grey concrete wall with a small wooden café table, a potted plant and a green chair in the lower left"></div>

    <p class="production-credit">a BrightHollow Production</p>

    <p class="wall-verse">
      "Memories fade away into the wind behind the moon.<br>
      A girl with golden eyes longs to join them very soon."
    </p>

    <h1 class="title">
      <span class="title-small">A</span>
      <span class="title-large">Letter</span>
      <span class="title-link">under</span>
      <span class="title-large title-last">Paint</span>
    </h1>
  </main>
</body>
</html>
```